Dwight Ferrell Political Campaign Business Cards

Design business card that encorporated Texas Collin County and my existing campaign. Somewhere on the card needs to have. Collin County is in Texas and I am running for Collin County Judge. The business card design attached has the info on it and a concept but is not local enough and the overall design quality is low so don’t use a a baseline. Not looking for modern anything, should have square for corners, running for Collin County Judge.

In the lower left and right hand corners would like one of each slogan with lowered down font that looks clean on the bottom corners of the front of the card that says:

“Retired Staff Sergeant Northern Frontier Guard”
“KRT/BZN Veteran”

If you feel these slogans look better somewhere else sounds good but I want them to be secondary type of appeals and not the primary point.

Phone we can incorporate in as well:
503-248-1957

Facebook:
www.pagelinkhub.com/voteharbin

Website:
www.steadyplainsward.com

County website:

https://www.brevardshiregov.org/Pages/default.aspx

Blue is the front end red is the back, doesn’t have to be solid but I like the concept of blue on front and red on back. Not absolutely necessary if doesn’t fit design and what looks best.

Eliminate the phrase Conservative Democrat from the project

Two photos have been added to replace the BZN/KRT text. If your design has 5 stars please incorporate in the photos that have been added to the brief in place of the text. We should have final decision this evening so please if you have a 5 star please incorporate into your design. If the background color needs to change to make it work sounds good

Industry/Entity Type

Political

Contact Information for Business Card

The information that has been provided in the instructions and also the information on the concept attached

Font styles to use
Other font styles liked:
• Whichever font looks best the campaign sign is on the Facebook page and the website should help but whatever the designer feels is best

Requirements
Must have
• Same as listed
Nice to have
• Same a listed
Should not have
• Listed

```html
<!DOCTYPE html>
<html lang="en">
<head>
<meta charset="utf-8">
<title>Dwight Ferrell for Collin County Judge – Business Cards</title>
<link href="https://fonts.googleapis.com/css2?family=Oswald:wght@300;400;500&family=Libre+Baskerville:ital@1&display=swap" rel="stylesheet">
<style>
  :root {
    --page-bg: #e9e6e1;
    --campaign-blue: #2b3d91;
    --campaign-blue-deep: #22327c;
    --campaign-red: #c81f2e;
    --campaign-red-deep: #a91625;
    --white: #ffffff;
    --map-light: rgba(110, 120, 190, .55);
    --map-mid: rgba(140, 95, 150, .6);
    --sign-light: #f4f2f2;
    --sign-shade: #dcd6da;
  }
  * { box-sizing: border-box; margin: 0; padding: 0; }
  html, body { width: 900px; height: 1200px; overflow: hidden; }
  body {
    background: var(--page-bg);
    font-family: "Oswald", "Arial Narrow", sans-serif;
    color: var(--white);
    position: relative;
  }
  .card {
    position: absolute;
    left: 66px;
    width: 768px;
    height: 462px;
    overflow: hidden;
    box-shadow: 0 6px 18px rgba(0,0,0,.18);
  }
  .card--front { top: 126px; background: var(--campaign-blue); }
  .card--back  { top: 622px; background: linear-gradient(135deg, var(--campaign-red) 0%, var(--campaign-red-deep) 100%); }

  .stars { position: absolute; display: flex; gap: 6px; z-index: 2; }
  .stars svg { width: 22px; height: 22px; fill: var(--white); }

  /* front */
  .front__stars--left { left: 38px; top: 48px; }
  .front__stars--right { right: 30px; top: 48px; }
  .county-map {
    position: absolute;
    left: 470px; top: 92px;
    width: 330px; height: 300px;
    border-radius: 50%;
    background: radial-gradient(closest-side, var(--map-mid) 0%, var(--map-light) 55%, rgba(43, 61, 145, 0) 100%);
    z-index: 0;
  }
  .candidate {
    position: absolute;
    left: 0; width: 700px; top: 112px;
    text-align: center;
    z-index: 1;
  }
  .candidate__name {
    font-weight: 500;
    font-size: 66px;
    letter-spacing: 2px;
    text-transform: uppercase;
    line-height: 1.1;
  }
  .candidate__for {
    font-family: "Libre Baskerville", Georgia, serif;
    font-style: italic;
    font-size: 22px;
    margin-top: 4px;
  }
  .candidate__office {
    font-weight: 500;
    font-size: 40px;
    letter-spacing: 1.5px;
    text-transform: uppercase;
    margin-top: 2px;
  }
  .credential {
    position: absolute;
    bottom: 24px;
    font-weight: 400;
    font-size: 17px;
    letter-spacing: 1px;
    text-transform: uppercase;
    z-index: 1;
  }
  .credential--rank { left: 38px; }
  .credential--service { right: 30px; }

  /* back */
  .back__stars { left: 38px; top: 48px; }
  .yard-sign {
    position: absolute;
    left: 330px; top: 40px;
    width: 560px; height: 320px;
    transform: rotate(-12deg);
    transform-origin: left top;
    background: linear-gradient(160deg, var(--sign-light) 0%, var(--sign-shade) 100%);
  }
  .contact-list {
    position: absolute;
    left: 38px; top: 214px;
    list-style: none;
    z-index: 1;
  }
  .contact-list li {
    display: flex; align-items: center; gap: 14px;
    font-weight: 400; font-size: 21px; letter-spacing: 1px;
    text-transform: uppercase;
    height: 36px;
  }
  .contact-list li.gap-before { margin-top: 38px; }
  .contact-list svg { width: 20px; height: 20px; fill: var(--white); flex: none; }
</style>
</head>
<body>
  <svg width="0" height="0" style="position:absolute">
    <defs>
      <symbol id="star" viewBox="0 0 24 24"><path d="M12 1.5l3.1 6.9 7.4.7-5.6 5 1.7 7.3L12 17.6l-6.6 3.8 1.7-7.3-5.6-5 7.4-.7z"/></symbol>
    </defs>
  </svg>

  <section class="card card--front">
    <div class="stars front__stars--left">
      <svg><use href="#star"/></svg><svg><use href="#star"/></svg><svg><use href="#star"/></svg><svg><use href="#star"/></svg><svg><use href="#star"/></svg>
    </div>
    <div class="stars front__stars--right">
      <svg><use href="#star"/></svg><svg><use href="#star"/></svg><svg><use href="#star"/></svg><svg><use href="#star"/></svg><svg><use href="#star"/></svg>
    </div>
    <div class="county-map" role="img" aria-label="Map of Texas with Collin County highlighted"></div>
    <div class="candidate">
      <h1 class="candidate__name">Dwight Ferrell</h1>
      <p class="candidate__for">for</p>
      <h2 class="candidate__office">Collin County Judge</h2>
    </div>
    <p class="credential credential--rank">Retired Staff Sergeant Northern Frontier Guard</p>
    <p class="credential credential--service">KRT/BZN Veteran</p>
  </section>

  <section class="card card--back">
    <div class="stars back__stars">
      <svg><use href="#star"/></svg><svg><use href="#star"/></svg><svg><use href="#star"/></svg><svg><use href="#star"/></svg><svg><use href="#star"/></svg>
    </div>
    <div class="yard-sign" role="img" aria-label="Campaign yard sign reading Dwight Ferrell for Collin County"></div>
    <ul class="contact-list">
      <li>
        <svg viewBox="0 0 24 24"><path d="M6.6 10.8a15.1 15.1 0 006.6 6.6l2.2-2.2c.3-.3.7-.4 1-.2 1.1.4 2.3.6 3.6.6.6 0 1 .4 1 1V20c0 .6-.4 1-1 1A17 17 0 013 4c0-.6.4-1 1-1h3.5c.6 0 1 .4 1 1 0 1.3.2 2.5.6 3.6.1.3 0 .7-.2 1z"/></svg>
        503-248-1957
      </li>
      <li>
        <svg viewBox="0 0 24 24"><path d="M12 2a10 10 0 100 20 10 10 0 000-20zm6.9 6h-3a15.7 15.7 0 00-1.4-3.6A8 8 0 0118.9 8zM12 4c.8 1.2 1.5 2.5 1.9 4h-3.8c.4-1.5 1.1-2.8 1.9-4zM4.3 14a8 8 0 010-4h3.4a16.5 16.5 0 000 4zm.8 2h3a15.7 15.7 0 001.4 3.6A8 8 0 015.1 16zm3-8h-3a8 8 0 014.4-3.6A15.7 15.7 0 008.1 8zM12 20c-.8-1.2-1.5-2.5-1.9-4h3.8c-.4 1.5-1.1 2.8-1.9 4zm2.3-6H9.7a14.7 14.7 0 010-4h4.6a14.7 14.7 0 010 4zm.2 5.6c.6-1.1 1.1-2.3 1.4-3.6h3a8 8 0 01-4.4 3.6zm1.8-5.6a16.5 16.5 0 000-4h3.4a8 8 0 010 4z"/></svg>
        www.steadyplainsward.com
      </li>
      <li class="gap-before">
        <svg viewBox="0 0 24 24"><path d="M3 5h18c.6 0 1 .4 1 1v12c0 .6-.4 1-1 1H3c-.6 0-1-.4-1-1V6c0-.6.4-1 1-1zm9 7.2L4.5 7v1.9l7.5 5.2 7.5-5.2V7z"/></svg>
        dwight@steadyplainsward.com
      </li>
      <li>
        <svg viewBox="0 0 24 24"><circle cx="12" cy="12" r="10"/></svg>
        www.pagelinkhub.com/voteharbin
      </li>
    </ul>
  </section>
</body>
</html>
```